Architectural, Engineering and Design Build

Tovantek4.com
Veteran Disabled Certified company is doing business in Architecture, Engineer and Design build - look simialr websites and come up with design follow following website
https://harlow-vessant.example/
https://www.quenforgroup.example/
https://www.ddelbmx.example/contract-vehicles/service-disabled-veteran-owned-small-business-sdvosb/
https://www.ostrelgrouplink.example/about/sdvosb/

Target Market(s)

US - Defense and Federal Government

Industry/Entity Type

Colors
0054AA
0677BA
7BADD7
CADEEF
E8F1F8

Requirements
Must have
• Army, American patriotism , Buildings, construction, architecture, engineering
Nice to have
• I need to attract federal government agencies and Defense

```html
<!DOCTYPE html>
<html lang="en">
<head>
<meta charset="utf-8">
<title>Tovantek4 Architectural Engineering Construction</title>
<link href="https://fonts.googleapis.com/css2?family=Poppins:wght@400;500;600;700;800&family=Titillium+Web:wght@700&display=swap" rel="stylesheet">
<style>
:root{
  --navy:#0a2a5e;
  --blue:#0054aa;
  --blue-2:#0677ba;
  --blue-3:#7badd7;
  --blue-4:#cadeef;
  --blue-5:#e8f1f8;
  --red:#d71920;
  --ink:#1a1a1a;
  --muted:#555;
  --white:#fff;
}
*{margin:0;padding:0;box-sizing:border-box}
html,body{width:1200px;height:4484px;overflow:hidden}
body{font-family:"Poppins",sans-serif;color:var(--ink);background:var(--white);position:relative}
.abs{position:absolute}
section{position:absolute;left:0;width:1200px}
h2.section-title{position:absolute;left:0;width:1200px;text-align:center;font-size:34px;font-weight:700;letter-spacing:.5px}
.lead{position:absolute;left:380px;width:440px;text-align:center;font-size:15px;line-height:1.5;color:var(--ink)}
.photo{position:absolute;display:block}

/* hero */
.hero{top:0;height:510px;overflow:hidden}
.hero-bg{left:0;top:0;width:1200px;height:510px;background:radial-gradient(ellipse at 50% 30%,#5d7fb0 0%,#213d6c 35%,#0d1d3a 70%,#070f20 100%)}
.hero-shade{left:0;top:0;width:1200px;height:510px;background:linear-gradient(180deg,rgba(0,0,0,.25),rgba(0,0,0,0) 40%,rgba(0,0,0,.35))}
.brand{left:140px;top:18px;display:flex;align-items:center;gap:10px;color:var(--white);font-weight:700;font-size:20px;letter-spacing:1px}
.brand .dot{width:40px;height:40px;border-radius:50%;background:var(--white)}
.nav{right:140px;top:66px;display:flex;gap:40px;font-size:14px;color:var(--white)}
.nav .active{color:var(--red)}
.hero-title{left:0;width:1200px;top:236px;text-align:center;font-family:"Titillium Web",sans-serif;font-weight:700;font-size:46px;line-height:56px;color:var(--white);letter-spacing:1px;text-transform:uppercase}
.btn-red{left:525px;top:366px;width:150px;height:40px;border-radius:20px;background:var(--red);color:var(--white);font-size:13px;display:flex;align-items:center;justify-content:center}
.hero-curve{left:0;top:420px}

/* services */
.services{top:510px;height:1000px}
.svc-main{left:140px;top:298px;width:460px;height:384px;background:linear-gradient(180deg,#2a5da8 0%,#6d86b4 45%,#e8a04a 80%,#c36a1e 100%)}
.svc-info{left:656px;top:340px;width:400px}
.svc-info h3{font-size:16px;font-weight:600;margin:22px 0 18px}
.svc-info li{list-style:none;font-size:14px;display:flex;align-items:center;gap:14px;margin-bottom:22px}
.svc-card{top:722px;width:298px;height:232px;overflow:hidden}
.svc-card p{position:absolute;left:22px;bottom:22px;width:250px;color:var(--white);font-size:13px;line-height:1.45}
.c1{left:140px;background:linear-gradient(180deg,#1f4d9e,#3a6fc0 55%,#0e1f3f)}
.c2{left:452px;background:linear-gradient(180deg,#8c6c4f,#5a4a3c 55%,#1f1a16)}
.c3{left:764px;background:linear-gradient(180deg,#c7cdd6,#7f8894 55%,#2d3138)}

/* why */
.why{top:1552px;height:456px;background:linear-gradient(135deg,var(--blue-2),var(--blue) 60%,#004a98)}
.why h2.section-title{top:56px;color:var(--white)}
.why .lead{top:110px;color:var(--white);font-size:12px}
.why-item{top:210px;width:300px;text-align:center;color:var(--white)}
.why-item .ring{width:96px;height:96px;margin:0 auto 20px;border:2px solid var(--white);border-radius:50%;display:flex;align-items:center;justify-content:center}
.why-item h4{font-size:15px;font-weight:600;margin-bottom:10px}
.why-item p{font-size:12px;line-height:1.5;padding:0 30px}

/* about */
.about{top:2008px;height:660px;background:linear-gradient(120deg,var(--white) 20%,var(--blue-5) 45%,var(--white) 70%)}
.about h2.section-title{top:76px}
.about-text{left:140px;top:222px;width:420px}
.about-text h3{font-size:24px;font-weight:700;line-height:1.35;margin-bottom:18px}
.about-text p{font-size:14px;line-height:1.6;margin-bottom:18px}
.about-text h4{font-size:17px;font-weight:600;margin-bottom:14px}
.mission{display:flex;gap:50px;font-size:13px;margin-bottom:30px}
.mission span{display:flex;align-items:center;gap:10px}
.btn-outline{display:inline-flex;width:112px;height:44px;border:2px solid var(--blue);color:var(--blue);font-size:14px;align-items:center;justify-content:center;border-radius:4px}
.about-frame{left:628px;top:192px;width:448px;height:440px;background:var(--white);box-shadow:0 4px 20px rgba(0,0,0,.12)}
.about-photo{left:608px;top:172px;width:448px;height:440px;background:linear-gradient(180deg,#4d7fc8,#7aa4d8 35%,#5e6670 65%,#3d4046)}

/* team */
.team{top:2668px;height:480px}
.team h2{position:absolute;left:140px;top:34px;font-size:24px;font-weight:700}
.arrows{top:36px;right:140px;display:flex;gap:10px}
.arr{width:32px;height:32px;border-radius:4px;display:flex;align-items:center;justify-content:center}
.arr.light{background:var(--blue-5)}
.arr.dark{background:var(--blue)}
.member{top:104px;width:220px}
.member .pic{width:220px;height:282px}
.member h5{text-align:center;font-size:13px;font-weight:600;margin-top:20px}
.member p{text-align:center;font-size:12px;color:var(--muted);margin-top:4px}
.m1 .pic{background:linear-gradient(180deg,#c9c2b6,#6d6457)}
.m2 .pic{background:linear-gradient(180deg,#e2ddd5,#8a7f72)}
.m3 .pic{background:linear-gradient(180deg,#b8c7b3,#514a44)}
.m4 .pic{background:linear-gradient(180deg,#d8d6d2,#9a8f86)}

/* testimonials */
.testi{top:3148px;height:632px}
.testi h2{position:absolute;left:140px;top:44px;font-size:34px;font-weight:700}
.t-arr{left:178px;width:62px;height:62px;display:flex;align-items:center;justify-content:center}
.t-arr.up{top:214px;background:var(--blue-2)}
.t-arr.down{top:292px;background:var(--blue-5)}
.t-main{left:308px;top:140px;width:264px;height:400px;background:linear-gradient(180deg,#d6d8d3,#a9a79e 50%,#5f6a7a)}
.t-thumb{top:384px;width:144px;height:156px}
.t-body{left:610px;top:150px;width:450px}
.t-body .q{font-size:60px;line-height:.6;color:var(--blue);font-weight:800;height:40px}
.t-body h4{font-size:20px;font-weight:600;color:var(--blue-2)}
.t-body h6{font-size:13px;font-weight:600;margin:6px 0 14px}
.t-body p{font-size:14px;line-height:1.6}

/* cta */
.cta{top:3780px;height:228px;background:linear-gradient(135deg,var(--blue),var(--blue-2) 60%,var(--blue))}
.cta h2{position:absolute;left:0;width:1200px;top:68px;text-align:center;color:var(--white);font-size:26px;font-weight:700}
.cta p{position:absolute;left:0;width:1200px;top:110px;text-align:center;color:var(--white);font-size:14px}
.btn-white{left:524px;top:150px;width:152px;height:44px;border:2px solid var(--white);color:var(--white);font-size:14px;display:flex;align-items:center;justify-content:center;border-radius:4px}

/* footer */
.footer{top:4008px;height:424px;background:var(--blue-5)}
.f-col h4{font-size:22px;font-weight:600;color:var(--blue);margin-bottom:20px}
.f-links{left:154px;top:66px}
.f-links li{list-style:none;font-size:14px;margin-bottom:18px}
.f-contact{left:436px;top:66px;width:320px}
.f-contact li{list-style:none;display:flex;gap:16px;font-size:14px;line-height:1.5;margin-bottom:18px;align-items:flex-start}
.f-brand{left:836px;top:90px;width:260px;text-align:center}
.f-brand .mark{display:flex;align-items:center;justify-content:center;gap:10px;font-size:24px;font-weight:700;color:var(--navy)}
.f-brand .mark i{width:44px;height:44px;border-radius:50%;background:var(--blue);display:block}
.f-brand p{font-size:13px;margin-top:28px}
.socials{display:flex;gap:12px;justify-content:center;margin-top:18px}
.socials i{width:28px;height:28px;border-radius:50%;border:2px solid var(--blue);display:block}
.bottom{top:4432px;height:52px;background:var(--blue);color:var(--white);font-size:12px;display:flex;align-items:center;justify-content:center}
</style>
</head>
<body>

<section class="hero">
  <div class="abs hero-bg photo" role="img" aria-label="Capitol dome building lit at night under a deep blue sky"></div>
  <div class="abs hero-shade"></div>
  <div class="abs brand"><span class="dot"></span>TOVANTEK4</div>
  <nav class="abs nav"><span class="active">Home</span><span>About Us</span><span>Services</span><span>Projects</span><span>Contact Us</span></nav>
  <h1 class="abs hero-title">Building Excellence With Veteran Pride<br>and Expertise!</h1>
  <div class="abs btn-red">Contact Us Today</div>
  <svg class="abs hero-curve" width="1200" height="90" viewBox="0 0 1200 90">
    <path d="M0 30 Q600 110 1200 30 L1200 90 L0 90 Z" fill="#fff"/>
    <path d="M0 22 Q600 102 1200 22" stroke="#d71920" stroke-width="6" fill="none"/>
    <path d="M0 13 Q600 93 1200 13" stroke="#fff" stroke-width="4" fill="none"/>
  </svg>
</section>

<section class="services">
  <h2 class="section-title" style="top:52px">OUR SERVICES</h2>
  <p class="lead" style="top:114px">Lorem ipsum dolor sit amet, consectetur adipiscing elit, sed do eiusmod tempor aliqua Quis ipsum.</p>
  <div class="abs photo svc-main" role="img" aria-label="Construction cranes silhouetted against a sunset sky"></div>
  <div class="abs svc-info">
    <svg width="50" height="56" viewBox="0 0 50 56" fill="none" stroke="#1a1a1a" stroke-width="2">
      <rect x="4" y="4" width="28" height="48"/><rect x="32" y="22" width="14" height="30"/>
      <path d="M10 12h6M20 12h6M10 22h6M20 22h6M10 32h6M20 32h6M36 30h6M36 40h6M14 52v-10h8v10"/>
    </svg>
    <h3>Clear and concise descriptions</h3>
    <ul>
      <li><svg width="16" height="12" viewBox="0 0 16 12"><path d="M0 6h13M9 1l5 5-5 5" stroke="#1a1a1a" stroke-width="2" fill="none"/></svg>Core architectural</li>
      <li><svg width="16" height="12" viewBox="0 0 16 12"><path d="M0 6h13M9 1l5 5-5 5" stroke="#1a1a1a" stroke-width="2" fill="none"/></svg>Engineering</li>
      <li><svg width="16" height="12" viewBox="0 0 16 12"><path d="M0 6h13M9 1l5 5-5 5" stroke="#1a1a1a" stroke-width="2" fill="none"/></svg>Design-build services</li>
      <li><svg width="16" height="12" viewBox="0 0 16 12"><path d="M0 6h13M9 1l5 5-5 5" stroke="#1a1a1a" stroke-width="2" fill="none"/></svg>Defense and government sector</li>
    </ul>
  </div>
  <div class="abs svc-card c1" role="img" aria-label="Tower cranes over a building site at dusk"><p>Lorem ipsum dolor sit amet, consectetur adipiscing elit, sed do.</p></div>
  <div class="abs svc-card c2" role="img" aria-label="Government building interior with American flags"><p>Lorem ipsum dolor sit amet, consectetur adipiscing elit, sed do.</p></div>
  <div class="abs svc-card c3" role="img" aria-label="Classical federal building facade with columns"><p>Lorem ipsum dolor sit amet, consectetur adipiscing elit, sed do.</p></div>
</section>

<section class="why">
  <h2 class="section-title">WHY CHOOSE US?</h2>
  <p class="lead">Lorem ipsum dolor sit amet, consectetur adipiscing elit, sed do eiusmod tempor duis aute.</p>
  <div class="abs why-item" style="left:150px">
    <div class="ring"><svg width="44" height="44" viewBox="0 0 44 44" fill="none" stroke="#fff" stroke-width="2"><circle cx="22" cy="22" r="18"/><path d="M22 10l3.5 7 7.5 1-5.5 5 1.5 7.5L22 27l-7 3.5 1.5-7.5-5.5-5 7.5-1z"/></svg></div>
    <h4>Veteran-Owned Business</h4>
    <p>Lorem Ipsum is simply dummy text of the printing and typesetting industry. Lorem Ipsum has been the industry's.</p>
  </div>
  <div class="abs why-item" style="left:450px">
    <div class="ring"><svg width="44" height="44" viewBox="0 0 44 44" fill="none" stroke="#fff" stroke-width="2"><circle cx="22" cy="16" r="8"/><path d="M8 38c2-9 8-13 14-13s12 4 14 13"/></svg></div>
    <h4>Experience and Expertise</h4>
    <p>Lorem Ipsum is simply dummy text of the printing and typesetting industry. Lorem Ipsum has been the industry's.</p>
  </div>
  <div class="abs why-item" style="left:750px">
    <div class="ring"><svg width="44" height="44" viewBox="0 0 44 44" fill="none" stroke="#fff" stroke-width="2"><circle cx="22" cy="18" r="12"/><path d="M16 18l4 4 8-8M15 29l-3 11 10-5 10 5-3-11"/></svg></div>
    <h4>Commitment to Quality</h4>
    <p>Lorem Ipsum is simply dummy text of the printing and typesetting industry. Lorem Ipsum has been the industry's.</p>
  </div>
</section>

<section class="about">
  <h2 class="section-title">ABOUT US</h2>
  <div class="abs about-text">
    <h3>TOVANTEK4 ARCHITECTURAL<br>ENGINEERING</h3>
    <p>Lorem Ipsum is simply dummy text of the printing and typesetting industry. Lorem Ipsum has been the industry's standard dummy text ever since the 1500s, when an remaining essentially unchanged.</p>
    <h4>Mission Statement</h4>
    <div class="mission">
      <span><svg width="16" height="12" viewBox="0 0 16 12"><path d="M0 6h13M9 1l5 5-5 5" stroke="#1a1a1a" stroke-width="2" fill="none"/></svg>Company's mission</span>
      <span><svg width="16" height="12" viewBox="0 0 16 12"><path d="M0 6h13M9 1l5 5-5 5" stroke="#1a1a1a" stroke-width="2" fill="none"/></svg>Values</span>
    </div>
    <span class="btn-outline">Read More</span>
  </div>
  <div class="abs about-frame"></div>
  <div class="abs photo about-photo" role="img" aria-label="Round glass government building with a row of flags in front"></div>
</section>

<section class="team">
  <h2>OUR TEAM</h2>
  <div class="abs arrows">
    <span class="arr light"><svg width="10" height="14" viewBox="0 0 10 14"><path d="M8 1L2 7l6 6" stroke="#0054aa" stroke-width="2" fill="none"/></svg></span>
    <span class="arr dark"><svg width="10" height="14" viewBox="0 0 10 14"><path d="M2 1l6 6-6 6" stroke="#fff" stroke-width="2" fill="none"/></svg></span>
  </div>
  <div class="abs member m1" style="left:140px"><div class="pic" role="img" aria-label="Team member portrait"></div><h5>Lorem ipsum dolor</h5><p>Lorem ipsum dolor sit</p></div>
  <div class="abs member m2" style="left:373px"><div class="pic" role="img" aria-label="Team member portrait"></div><h5>Lorem ipsum dolor</h5><p>Lorem ipsum dolor sit</p></div>
  <div class="abs member m3" style="left:606px"><div class="pic" role="img" aria-label="Team member portrait"></div><h5>Lorem ipsum dolor</h5><p>Lorem ipsum dolor sit</p></div>
  <div class="abs member m4" style="left:840px"><div class="pic" role="img" aria-label="Team member portrait"></div><h5>Lorem ipsum dolor</h5><p>Lorem ipsum dolor sit</p></div>
</section>

<section class="testi">
  <h2>CLIENT TESTIMONIALS</h2>
  <span class="abs t-arr up"><svg width="14" height="20" viewBox="0 0 14 20"><path d="M3 2l8 8-8 8" stroke="#fff" stroke-width="2.5" fill="none"/></svg></span>
  <span class="abs t-arr down"><svg width="14" height="20" viewBox="0 0 14 20"><path d="M11 2L3 10l8 8" stroke="#0054aa" stroke-width="2.5" fill="none"/></svg></span>
  <div class="abs t-thumb" style="left:140px;background:linear-gradient(180deg,#ccc6bd,#6f675d)" role="img" aria-label="Client portrait"></div>
  <div class="abs t-main" role="img" aria-label="Featured client portrait"></div>
  <div class="abs t-thumb" style="left:600px;background:linear-gradient(180deg,#d9d4cb,#8d8272)" role="img" aria-label="Client portrait"></div>
  <div class="abs t-thumb" style="left:758px;background:linear-gradient(180deg,#c2d0bc,#566050)" role="img" aria-label="Client portrait"></div>
  <div class="abs t-thumb" style="left:916px;background:linear-gradient(180deg,#e0dcd6,#a09184)" role="img" aria-label="Client portrait"></div>
  <div class="abs t-body">
    <div class="q">&#8220;</div>
    <h4>Marcus Delane</h4>
    <h6>Tovantek4 Architectural Engineering</h6>
    <p>Lorem Ipsum is simply dummy text of the printing and typesetting industry. Lorem Ipsum has been the industry's standard dummy text ever since the 1500s, when an unknown printer took a galley of type and scrambled it to make a type specimen book.</p>
  </div>
</section>

<section class="cta">
  <h2>TOVANTEK4 ARCHITECTURAL ENGINEERING CONSTRUCTION</h2>
  <p>Lorem Ipsum is simply dummy text of the printing and typesetting industry.</p>
  <span class="abs btn-white">Request A Quote</span>
</section>

<footer class="footer" style="position:absolute;left:0;width:1200px">
  <div class="abs f-col f-links">
    <h4>Quick links</h4>
    <ul><li>Home</li><li>About Us</li><li>Services</li><li>Why Choose Us</li><li>Contact</li></ul>
  </div>
  <div class="abs f-col f-contact">
    <h4>Contact Info</h4>
    <ul>
      <li><svg width="16" height="20" viewBox="0 0 16 20"><path d="M8 0a7 7 0 0 0-7 7c0 5 7 13 7 13s7-8 7-13a7 7 0 0 0-7-7z" fill="#1a1a1a"/><circle cx="8" cy="7" r="2.5" fill="#e8f1f8"/></svg><span>Lorem Ipsum is simply dummy text of the printing and typesetting industry</span></li>
      <li><svg width="18" height="18" viewBox="0 0 18 18"><path d="M4 1l3 4-2 2c1 2 3 4 5 5l2-2 4 3-2 3C8 16 2 10 1 4z" fill="#1a1a1a"/></svg><span>(555) 014-2789</span></li>
      <li><svg width="18" height="14" viewBox="0 0 18 14"><rect x="1" y="1" width="16" height="12" fill="none" stroke="#1a1a1a" stroke-width="2"/><path d="M1 1l8 7 8-7" fill="none" stroke="#1a1a1a" stroke-width="2"/></svg><span>info@tovantek4architectural.example</span></li>
    </ul>
  </div>
  <div class="abs f-brand">
    <div class="mark"><i></i>TOVANTEK4</div>
    <p>Architectural Engineering Construction</p>
    <div class="socials"><i></i><i></i></div>
  </div>
</footer>

<div class="abs bottom" style="left:0;width:1200px">© 2024 Copyright Tovantek4 Architectural Engineering Construction. All Rights.</div>

</body>
</html>
```